Gordon Pellbrook Consulting - Web Design Project

We need a web design for my new edgy consulting business specializing in innovation, technology and strategy.

It is our personal goal to turn each client into raving fans by helping them achieve their own business goals and aspirations through assisting them in raising their own innovation and marketing standards.

We provide our personalised and state-of-the-art services to our clients and boards who represent some of the world greatest innovative thinkers.
Updates

Here is some other information which may help shape your thinking.

I've had direct Involvement in the development of the following iPad, iPhone Applications and websites

FarbeyondOzlands.com (TerraLink platform) by Voyage Bureau
http://farbeyondozlands.example.au

Sail Verve by Bright Voyaging
https://apps.example-store.com/au/app/sail-verve/id100000001

uRedlandTR by Travel Territory Board
https://apps.example-store.com/au/app/uredlandtr/id100000002

Wexmoor Trips
http://www.wexmoortrips.example.au

Trek Mapper by Voyage Bureau
http://apps.example-store.com/au/app/trek-mapper/id100000003

Sunward by Sunward Travel Office
https://apps.example-store.com/au/app/sunward/id100000004

Upper Fernridge Valley Route by Visit Coastlands
https://apps.example-store.com/au/app/upper-fernridge-valley-route/id100000005

Wanderer Path by Travel Territory Board and Southern Plains Travel Council
https://apps.example-store.com/au/app/wanderers-path-grand-journey/id100000006

Gordon Pellbrook Consulting (GPC)
November 2012 – Present (8 months)Brisbane, Sydney, Canberra

Gordon’s consults to Small-to-Medium Enterprises (SME) and Government organisations on business strategy, technology strategy, risk mitigation, disruptive technology and innovation in the workplace.

Gordon’s consultancy mantra is that we cannot divorce economic life from cultural life particularly in an era when social capital may be as important as physical capital in business.

Reason: request from designers, I want to see their best efforts

Target Market(s)

35+

Industry/Entity Type

Business

Requirements
Must have
• Please use some of the personal image(s) contained in the zip files which can be downloaded from here

http://filedrop.example/k9Xq2Lm
http://filedrop.example/p4Rt7Vn
http://filedrop.example/z8Hw3Bc
Nice to have
• Black, Sleek design, maybe minimalist. Nice to have a Pixelle for the design. Nice to have it easily ported to Wordpress or be a modified Wordpress template. HTML 5, responsive design

```html
<!DOCTYPE html>
<html lang="en">
<head>
<meta charset="utf-8">
<title>Gordon Pellbrook Consulting</title>
<link rel="stylesheet" href="https://fonts.googleapis.com/css2?family=Open+Sans:wght@400;600;700&family=Oswald:wght@400;500&display=swap">
<style>
:root{
  --black:#0d0d0d;
  --hero:#1a1a1a;
  --orange:#e8621c;
  --green:#6fae1e;
  --green-dark:#4f8a10;
  --panel:#d4d4d4;
  --content:#e4e4e4;
  --footer:#8c8c8c;
  --base:#c9c9c9;
  --text:#4a4a4a;
  --heading:#6a6a6a;
  --white:#ffffff;
  --rule:#b5b5b5;
}
*{box-sizing:border-box;margin:0;padding:0}
html,body{width:735px;height:1200px;overflow:hidden}
body{background:var(--base);font-family:"Open Sans",Arial,sans-serif;color:var(--text);position:relative}
.site-header{position:absolute;top:0;left:0;width:735px;height:60px;background:var(--black);z-index:2}
.brand{position:absolute;left:55px;top:14px;color:var(--white);font:700 26px/32px "Open Sans",Arial,sans-serif;letter-spacing:1px}
.main-nav{position:absolute;right:30px;top:40px;display:flex;gap:0}
.main-nav a{color:var(--white);text-decoration:none;font-size:11px;padding:0 14px;border-left:1px solid #555}
.main-nav a:first-child{border-left:none}
.main-nav a.is-active{color:var(--orange)}
.hero{position:absolute;top:60px;left:0;width:735px;height:380px;background:
  radial-gradient(ellipse at 55% 30%,#333 0%,transparent 60%),
  repeating-linear-gradient(135deg,#1c1c1c 0 6px,#202020 6px 7px),var(--hero)}
.hero-photo{position:absolute;right:30px;top:0;width:275px;height:380px;background:linear-gradient(180deg,#5a5a5a 0%,#8a8f96 45%,#6b7684 100%)}
.hero-title{position:absolute;left:50px;top:112px;color:var(--orange);font:400 23px/28px "Open Sans",Arial,sans-serif}
.hero-meta{position:absolute;left:50px;top:146px;color:var(--white);font-size:11px;font-weight:600}
.hero-text{position:absolute;left:50px;top:190px;width:235px;color:#d8d8d8;font-size:10.5px;line-height:15px}
.services{position:absolute;top:440px;left:0;width:735px;height:235px;background:var(--panel);display:flex;padding:0 35px}
.service{flex:1;text-align:center;padding:18px 14px 0;border-left:1px solid var(--rule)}
.service:first-child{border-left:none}
.service svg{display:block;margin:0 auto;width:40px;height:40px}
.service h2{color:var(--orange);font:400 22px/28px "Oswald",Arial,sans-serif;margin-top:12px}
.service p{font-size:9.5px;line-height:14px;margin-top:8px;min-height:56px}
.btn{display:inline-block;margin-top:14px;background:linear-gradient(var(--green),var(--green-dark));color:var(--white);font-size:10px;padding:5px 14px;border-radius:2px;text-decoration:none}
.content{position:absolute;top:675px;left:0;width:735px;height:270px;background:var(--content)}
.welcome{position:absolute;left:85px;top:14px;width:335px}
.content h3{color:var(--heading);font:500 17px/22px "Oswald",Arial,sans-serif;border-bottom:1px solid var(--rule);padding-bottom:6px}
.welcome p,.support p{font-size:9.5px;line-height:14px;margin-top:10px}
.support{position:absolute;left:85px;top:165px;width:335px}
.news{position:absolute;left:450px;top:14px;width:230px}
.news-item{margin-top:10px;font-size:9.5px;line-height:13px}
.news-date{font-weight:700;color:#333}
.news-more{display:block;text-align:right;color:var(--orange);font-size:8.5px;text-decoration:none}
.site-footer{position:absolute;top:945px;left:0;width:735px;height:135px;background:var(--footer)}
.copyright{position:absolute;right:85px;top:55px;color:#2f2f2f;font-size:9px}
</style>
</head>
<body>
<header class="site-header">
  <div class="brand">GPC</div>
  <nav class="main-nav">
    <a href="#" class="is-active">Home</a><a href="#">About</a><a href="#">Service</a><a href="#">Clients</a><a href="#">Contact</a>
  </nav>
</header>

<section class="hero">
  <h1 class="hero-title">Gordon Pellbrook Consulting</h1>
  <p class="hero-meta">November 2012 – Present (8 months)Brisbane, Sydney, Canberra</p>
  <p class="hero-text">Gordon’s consults to Small-to-Medium Enterprises (SME) and Government organisations on business strategy, technology strategy, risk mitigation, disruptive technology and innovation in the workplace.</p>
  <div class="hero-photo" role="img" aria-label="Portrait photograph of Gordon Pellbrook in a grey suit"></div>
</section>

<section class="services">
  <article class="service">
    <svg viewBox="0 0 40 40" fill="none" stroke="#666" stroke-width="2"><circle cx="20" cy="16" r="9"/><path d="M16 26h8M16 30h8M18 34h4"/></svg>
    <h2>Innovation</h2>
    <p>Fresh thinking turns everyday problems into lasting growth. We help leaders test new ideas quickly and bring the best of them to market.</p>
    <a class="btn" href="#">Learn More...</a>
  </article>
  <article class="service">
    <svg viewBox="0 0 40 40" fill="none" stroke="#666" stroke-width="2.5" stroke-linecap="round"><path d="M6 18a20 20 0 0 1 28 0M11 23a13 13 0 0 1 18 0M16 28a6 6 0 0 1 8 0"/><circle cx="20" cy="33" r="1.8" fill="#666"/></svg>
    <h2>Technology</h2>
    <p>Smart systems should serve people first. We review your tools, plan sensible upgrades and keep every project on budget and on time.</p>
    <a class="btn" href="#">Learn More...</a>
  </article>
  <article class="service">
    <svg viewBox="0 0 40 40" fill="none" stroke="#666" stroke-width="2" stroke-linejoin="round"><path d="M16 5h8M17 5v11L8 34h24L23 16V5"/></svg>
    <h2>Strategy</h2>
    <p>Clear direction beats busy effort. We map risks, set priorities and shape a plan your board can act on with confidence.</p>
    <a class="btn" href="#">Learn More...</a>
  </article>
</section>

<section class="content">
  <div class="welcome">
    <h3>Welcome</h3>
    <p>Every engagement starts with listening. We spend time understanding your business, your people and your market before we suggest a single change. From there we build a practical roadmap, work alongside your team and measure what matters, so that new ideas turn into real results that last well beyond our time with you.</p>
  </div>
  <div class="support">
    <h3>Technical Support</h3>
    <p>Need a hand after launch? Our support team keeps your platforms secure, up to date and running smoothly, with clear reports and fast answers whenever questions come up.</p>
  </div>
  <aside class="news">
    <h3>Latest News</h3>
    <div class="news-item"><div class="news-date">May 13</div>New workshop series on digital strategy for small firms opens for bookings this month.<a class="news-more" href="#">Read More</a></div>
    <div class="news-item"><div class="news-date">May 25</div>Gordon joins a government panel on workplace innovation and shares early findings.<a class="news-more" href="#">Read More</a></div>
    <div class="news-item"><div class="news-date">June 18</div>Case study: how a regional tourism app doubled its users within one season.<a class="news-more" href="#">Read More</a></div>
  </aside>
</section>

<footer class="site-footer">
  <p class="copyright">Copyright © 2013 Gordon Pellbrook Consulting</p>
</footer>
</body>
</html>
```